Quorvex - Automated robotic Inspection with AI need new business cards

We need a new design of our business cards. The company is focused on automated quality control at high speed with unmatched results. We have a logo but need a more forward leaning business card that shows that we are delivering cutting edge technology.

Contact Information for Business Card

Name
Position
Adress
Phone
Email
e.g.
Lena Holmqvist
Chief Financial Officer (CFO)

Quorvex Sweden AB
Bruksvägen 14, SE-175 43 JÄRFÄLLA, Sweden
Mobile: +46735 21 47 83 | Office: +46 8 61 94 27
www.quorvex-example.com

Font styles to use
Sans Serif

```html
<!DOCTYPE html>
<html lang="en">
<head>
<meta charset="utf-8">
<title>Quorvex business cards</title>
<link rel="stylesheet" href="https://fonts.googleapis.com/css2?family=Roboto:wght@400;700&display=swap">
<style>
  :root {
    --brand-blue: #1a5583;
    --brand-blue-dark: #134670;
    --brand-blue-light: #22628f;
    --ink: #1d4f7c;
    --paper: #ffffff;
    --backdrop: #e7eaed;
    --ghost: #eef2f6;
  }
  * { margin: 0; padding: 0; box-sizing: border-box; }
  html, body { width: 1200px; height: 900px; overflow: hidden; }
  body {
    background: var(--backdrop);
    font-family: "Roboto", Arial, sans-serif;
    display: flex;
    flex-direction: column;
    align-items: center;
    justify-content: center;
    gap: 40px;
  }
  .card {
    position: relative;
    width: 700px;
    height: 400px;
    overflow: hidden;
    box-shadow: 0 6px 18px rgba(20, 40, 60, 0.15);
  }
  .card-front {
    background: linear-gradient(135deg, var(--brand-blue-dark), var(--brand-blue) 55%, var(--brand-blue-light));
  }
  .card-back { background: var(--paper); }

  .ghost-circle {
    position: absolute;
    border-radius: 50%;
  }
  .card-front .ghost-circle {
    width: 420px; height: 420px;
    left: 150px; top: -10px;
    background: rgba(255, 255, 255, 0.05);
  }
  .card-back .ghost-circle {
    width: 380px; height: 380px;
    left: 150px; top: 10px;
    background: var(--ghost);
  }

  .wordmark {
    position: absolute;
    display: flex;
    align-items: center;
    gap: 18px;
    font-weight: 700;
    letter-spacing: 0.02em;
  }
  .wordmark-dot { border-radius: 50%; flex: none; }
  .card-front .wordmark {
    left: 50%; top: 50%;
    transform: translate(-50%, -50%);
    color: var(--paper);
    font-size: 84px;
  }
  .card-front .wordmark-dot { width: 58px; height: 58px; background: var(--paper); }
  .card-back .wordmark {
    left: 48px; top: 232px;
    color: var(--ink);
    font-size: 46px;
  }
  .card-back .wordmark-dot { width: 32px; height: 32px; background: var(--ink); }

  .divider {
    position: absolute;
    left: 372px; top: 120px;
    width: 1px; height: 200px;
    background: var(--ink);
  }
  .contact {
    position: absolute;
    left: 396px; top: 70px;
    color: var(--ink);
    font-size: 14px;
    line-height: 1.35;
  }
  .contact-name { font-size: 26px; font-weight: 700; line-height: 1.1; }
  .contact-role { font-size: 15px; margin-bottom: 18px; }
  .contact-address { margin-bottom: 18px; }
  .contact-lines { list-style: none; }
  .contact-lines li { display: flex; align-items: center; gap: 8px; margin-bottom: 3px; }
  .contact-icon { width: 14px; height: 14px; flex: none; }
</style>
</head>
<body>

  <section class="card card-front" aria-label="Card front">
    <div class="ghost-circle"></div>
    <div class="wordmark"><span class="wordmark-dot"></span>Quorvex</div>
  </section>

  <section class="card card-back" aria-label="Card back">
    <div class="ghost-circle"></div>
    <div class="wordmark"><span class="wordmark-dot"></span>Quorvex</div>
    <div class="divider"></div>
    <div class="contact">
      <p class="contact-name">Lena Holmqvist</p>
      <p class="contact-role">Chief Financial Officer (CFO)</p>
      <p class="contact-address">Quorvex Sweden AB<br>Bruksvägen 14,<br>SE-175 43 JÄRFÄLLA, Sweden</p>
      <ul class="contact-lines">
        <li>
          <svg class="contact-icon" viewBox="0 0 14 14" aria-hidden="true"><circle cx="7" cy="7" r="7" fill="#1d4f7c"/><rect x="4.5" y="3" width="5" height="8" rx="1" fill="#fff"/></svg>
          +46735 21 47 83
        </li>
        <li>
          <svg class="contact-icon" viewBox="0 0 14 14" aria-hidden="true"><circle cx="7" cy="7" r="7" fill="#1d4f7c"/><path d="M4 5.5 Q7 3 10 5.5 L9 6.5 L8 6 L8 8 L10 10 L4 10 L6 8 L6 6 L5 6.5 Z" fill="#fff"/></svg>
          +46 8 61 94 27
        </li>
        <li>
          <svg class="contact-icon" viewBox="0 0 14 14" aria-hidden="true"><circle cx="7" cy="7" r="7" fill="#1d4f7c"/><circle cx="7" cy="7" r="4" fill="none" stroke="#fff" stroke-width="1"/><path d="M3 7 H11 M7 3 V11" stroke="#fff" stroke-width="1"/></svg>
          www.quorvex-example.com
        </li>
      </ul>
    </div>
  </section>

</body>
</html>
```